Chicago Train Advertisement for HomeAlongRail.com.

We have purchased one month of advertising on the Chicago NRX subway train. We will have 150 cards up in the subway to advertise our website HomeAlongRail.com where people can search for properties by train station. The cards are 11" tall and 46.5" long. We want people to feel compelled to jump on their cell phones and conduct a search for an apartment or home while they are riding the train, or at least enter their email and search criteria so one of our agents can help them.

Target Market(s)

People who want to live near train stations

Industry/Entity Type

Real Estate

Font styles to use
Sans Serif

Colors

Designer to choose colors to be used in the design.

Requirements
Must have
• The homealongrail logo and a catchy slogan, something like: Find your home near a train station the easy way: www.homealongral.com. Search real estate listings near the NRX or Velco.

```html
<!DOCTYPE html>
<html lang="en">
<head>
<meta charset="utf-8">
<title>HomeAlongRail.com – Train Card</title>
<link href="https://fonts.googleapis.com/css2?family=Arimo:wght@400;700&display=swap" rel="stylesheet">
<style>
  :root {
    --sky: #a3dcf2;
    --sky-pattern: #92d1ec;
    --navy: #1d1f5c;
    --white: #ffffff;
    --brand-blue: #2d8fd0;
  }
  html, body {
    margin: 0;
    padding: 0;
    width: 1200px;
    height: 284px;
    overflow: hidden;
    background: var(--sky);
  }
  .card {
    position: relative;
    width: 1200px;
    height: 284px;
    overflow: hidden;
    font-family: "Arimo", Arial, sans-serif;
    color: var(--navy);
  }
  .backdrop {
    position: absolute;
    inset: 0;
    background: linear-gradient(180deg, var(--sky) 0%, var(--sky-pattern) 50%, var(--sky) 100%);
  }
  .headline {
    position: absolute;
    left: 52px;
    top: 52px;
    margin: 0;
    font-size: 44px;
    font-weight: 700;
    line-height: 55px;
    letter-spacing: -0.2px;
  }
  .brand {
    position: absolute;
    left: 52px;
    top: 232px;
    display: flex;
    align-items: center;
    gap: 8px;
    font-size: 17px;
    font-weight: 700;
    color: var(--navy);
  }
  .brand-dot {
    width: 14px;
    height: 14px;
    border-radius: 50%;
    background: var(--brand-blue);
  }
  .call-to-action {
    position: absolute;
    left: 752px;
    top: 150px;
  }
  .site-url {
    margin: 0;
    font-size: 34px;
    font-weight: 700;
    line-height: 38px;
    color: var(--white);
  }
  .search-note {
    margin: 8px 0 0;
    font-size: 24px;
    font-weight: 400;
    line-height: 28px;
    color: var(--navy);
  }
</style>
</head>
<body>
  <main class="card">
    <div class="backdrop" role="img" aria-label="Repeating pattern of light blue house outlines"></div>

    <h1 class="headline">Find your home near a train<br>station the easy way.</h1>

    <div class="brand">
      <span class="brand-dot"></span>
      <span class="brand-name">HomeAlongRail.com</span>
    </div>

    <section class="call-to-action">
      <p class="site-url">www.homealongral.com</p>
      <p class="search-note">Search real estate listings near<br>the NRX or Velco.</p>
    </section>
  </main>
</body>
</html>
```